Business card design for strategy and management consulting company. Would like to have a clean and professional business card, based on the attached logo. The company is a strategy and management consulting company focusing on sustainable business modlels based on economic, social and environmental market opportunities. Preferably the logo should be included on both sides of the design.

Industry/Entity Type

Business

Contact Information for Business Card

Halvor Brekkeli, CEO/Management consultant
halvor.brekkeli@morvikpartners.example
Mob: +47 936 28 417
Office: Lyngvedens gate 14, pb 312 sentrum, N-0158 Oslo Norway

Requirements
Must have
• Include attached logo
Nice to have
• Would like to have the logo on both sides
Should not have
• Many colours.

```html
<!DOCTYPE html>
<html lang="en">
<head>
<meta charset="utf-8">
<title>Morvik business card</title>
<link rel="stylesheet" href="https://fonts.googleapis.com/css2?family=Questrial&display=swap">
<style>
  :root {
    --backdrop: #d9d6d2;
    --card: #161616;
    --ink: #ffffff;
    --accent: #f2d40c;
    --muted: #e9e9e9;
  }
  * { margin: 0; padding: 0; box-sizing: border-box; }
  html, body { width: 1200px; height: 780px; overflow: hidden; }
  body {
    background: var(--backdrop);
    font-family: "Questrial", "Century Gothic", sans-serif;
    color: var(--ink);
    position: relative;
  }
  .card {
    position: absolute;
    top: 235px;
    width: 540px;
    height: 310px;
    border-radius: 16px;
    background: var(--card);
    box-shadow: 0 10px 30px rgba(0,0,0,0.25);
    overflow: hidden;
  }
  .card--front { left: 40px; }
  .card--back { left: 620px; }

  .wordmark {
    position: absolute;
    font-size: 62px;
    letter-spacing: 0.5px;
    line-height: 1;
    color: var(--ink);
    white-space: nowrap;
  }
  .card--front .wordmark { right: 70px; top: 62px; }
  .card--back .wordmark { left: 50%; top: 50%; transform: translate(-50%, -50%); font-size: 72px; }

  .rule { position: absolute; }
  .rule--accent { left: 0; top: 214px; width: 98px; height: 3px; background: var(--accent); }
  .rule--main { left: 112px; top: 208px; width: 390px; height: 2.5px; background: var(--ink); }

  .holder { position: absolute; left: 112px; top: 164px; }
  .holder__name { font-size: 15px; letter-spacing: 0.6px; text-transform: uppercase; }
  .holder__title { font-size: 13px; color: var(--accent); margin-top: 2px; }

  .address {
    position: absolute; right: 38px; top: 168px;
    font-size: 12px; line-height: 16px; color: var(--muted); font-style: normal;
    text-align: left;
  }

  .contact { position: absolute; left: 112px; top: 222px; list-style: none; }
  .contact__item { display: flex; align-items: center; gap: 8px; font-size: 12.5px; color: var(--muted); height: 19px; }
  .contact__icon { width: 14px; height: 14px; flex: none; }
</style>
</head>
<body>
  <section class="card card--front" aria-label="Card front">
    <div class="wordmark">Morvik</div>

    <div class="holder">
      <p class="holder__name">Halvor Brekkeli</p>
      <p class="holder__title">CEO/Management consultant</p>
    </div>

    <address class="address">
      Lyngvedens gate 14<br>
      pb 312 sentrum, N-0158 Oslo Norway
    </address>

    <div class="rule rule--accent"></div>
    <div class="rule rule--main"></div>

    <ul class="contact">
      <li class="contact__item">
        <svg class="contact__icon" viewBox="0 0 14 14" aria-hidden="true">
          <rect x="0" y="0" width="14" height="14" rx="2" fill="var(--accent)"/>
          <path d="M3 5.5 Q7 2.5 11 5.5 L10 7 L8.5 6.3 L8.5 5.4 Q7 5 5.5 5.4 L5.5 6.3 L4 7 Z M4.5 8 H9.5 L10.5 11 H3.5 Z" fill="var(--card)"/>
        </svg>
        +47 936 28 417
      </li>
      <li class="contact__item">
        <svg class="contact__icon" viewBox="0 0 14 14" aria-hidden="true">
          <rect x="0" y="0" width="14" height="14" rx="2" fill="var(--accent)"/>
          <rect x="2.5" y="4" width="9" height="6.5" fill="none" stroke="var(--card)" stroke-width="1.2"/>
          <path d="M2.5 4 L7 8 L11.5 4" fill="none" stroke="var(--card)" stroke-width="1.2"/>
        </svg>
        halvor.brekkeli@morvikpartners.example
      </li>
    </ul>
  </section>

  <section class="card card--back" aria-label="Card back">
    <div class="wordmark">Morvik</div>
  </section>
</body>
</html>
```